Business Card For Life Coaching Business For Men

Take my existing logo and apply it to a business card. I would like the logo to be prominent with stylistic text below reading Life Coaching For Men. Contact info should show as:
Gideon Marsh
gideon@bravepathgrowth.com

```html
<!DOCTYPE html>
<html lang="en">
<head>
<meta charset="utf-8">
<title>Brave Path Growth – Business Card</title>
<link href="https://fonts.googleapis.com/css2?family=Oswald:wght@500;600&family=Roboto:wght@400;500&display=swap" rel="stylesheet">
<style>
  :root {
    --backdrop: #3a3a3a;
    --backdrop-dark: #262626;
    --navy: #0a1190;
    --navy-deep: #050d7a;
    --teal: #0a8582;
    --teal-light: #0f8d88;
    --white: #ffffff;
    --ink: #333333;
    --divider: #c9c9c9;
  }
  * { box-sizing: border-box; margin: 0; padding: 0; }
  html, body { width: 1200px; height: 689px; overflow: hidden; }
  body {
    background: linear-gradient(135deg, var(--backdrop) 0%, var(--backdrop-dark) 100%);
    position: relative;
    font-family: "Roboto", Arial, sans-serif;
  }
  .card {
    position: absolute;
    width: 530px;
    height: 304px;
    border-radius: 18px;
    overflow: hidden;
    box-shadow: 0 14px 30px rgba(0,0,0,0.45);
  }
  /* Front */
  .card--front {
    left: 40px;
    top: 192px;
    background: linear-gradient(160deg, var(--teal-light) 0%, #066f8e 40%, var(--navy-deep) 85%);
  }
  .front__brand {
    position: absolute;
    left: 250px;
    top: 96px;
    display: flex;
    align-items: center;
    gap: 14px;
  }
  .front__dot {
    width: 22px; height: 22px; border-radius: 50%;
    background: var(--white);
    flex: none;
  }
  .front__name {
    font-family: "Oswald", sans-serif;
    font-weight: 600;
    font-size: 40px;
    line-height: 0.95;
    letter-spacing: 0.5px;
    color: var(--white);
    text-transform: uppercase;
  }
  .front__tagline {
    margin-top: 10px;
    font-family: "Roboto", sans-serif;
    font-weight: 500;
    font-size: 12px;
    letter-spacing: 2px;
    color: var(--white);
    text-transform: uppercase;
  }
  /* Back */
  .card--back {
    left: 630px;
    top: 192px;
    background: var(--white);
  }
  .back__band { position: absolute; left: 0; top: 0; width: 530px; height: 304px; }
  .back__brand {
    position: absolute;
    left: 30px;
    top: 82px;
    display: flex;
    align-items: center;
    gap: 12px;
  }
  .back__dot { width: 18px; height: 18px; border-radius: 50%; background: var(--navy); flex: none; }
  .back__name {
    font-family: "Oswald", sans-serif;
    font-weight: 600;
    font-size: 30px;
    line-height: 0.95;
    color: var(--navy);
    text-transform: uppercase;
  }
  .back__tagline {
    margin-top: 8px;
    font-family: "Roboto", sans-serif;
    font-weight: 500;
    font-size: 10px;
    letter-spacing: 1.4px;
    color: var(--teal);
    text-transform: uppercase;
  }
  .back__divider {
    position: absolute;
    left: 246px; top: 50px;
    width: 1px; height: 112px;
    background: var(--divider);
  }
  .back__person {
    position: absolute;
    left: 268px; top: 52px;
  }
  .person__name {
    font-family: "Oswald", sans-serif;
    font-weight: 500;
    font-size: 26px;
    line-height: 1.2;
    text-transform: uppercase;
    margin-bottom: 12px;
  }
  .person__first { color: var(--navy); }
  .person__last { color: var(--teal); }
  .contact { list-style: none; }
  .contact__item {
    display: flex; align-items: center; gap: 8px;
    font-size: 13px; line-height: 1.2; color: var(--ink);
    margin-bottom: 5px;
  }
  .contact__item svg { width: 13px; height: 13px; flex: none; }
  .contact__web { color: var(--navy); }
  .back__seal {
    position: absolute;
    left: 470px; top: 152px;
    width: 52px; height: 52px; border-radius: 50%;
    background: var(--white);
    border: 2px solid var(--teal);
  }
</style>
</head>
<body>

  <section class="card card--front">
    <div class="front__brand">
      <span class="front__dot"></span>
      <div>
        <h1 class="front__name">Brave Path<br>Growth</h1>
        <p class="front__tagline">Life Coaching For Men</p>
      </div>
    </div>
  </section>

  <section class="card card--back">
    <svg class="back__band" viewBox="0 0 530 304" aria-hidden="true">
      <polygon points="0,270 530,186 530,304 0,304" fill="var(--navy)"/>
      <line x1="0" y1="262" x2="530" y2="178" stroke="var(--teal)" stroke-width="4"/>
    </svg>

    <div class="back__brand">
      <span class="back__dot"></span>
      <div>
        <h2 class="back__name">Brave Path<br>Growth</h2>
        <p class="back__tagline">Life Coaching For Men</p>
      </div>
    </div>

    <div class="back__divider"></div>

    <div class="back__person">
      <p class="person__name"><span class="person__first">Gideon</span> <span class="person__last">Marsh</span></p>
      <ul class="contact">
        <li class="contact__item">
          <svg viewBox="0 0 16 16"><path fill="var(--navy)" d="M3.6 1.5l2.2 2.8-1.3 1.6c.9 2 2.6 3.7 4.6 4.6l1.6-1.3 2.8 2.2-1.4 2.3C6.8 14 2 9.2 1.3 2.9z"/></svg>
          <span>044-987 654 321</span>
        </li>
        <li class="contact__item">
          <svg viewBox="0 0 16 16"><rect x="1" y="3" width="14" height="10" fill="var(--navy)"/><path d="M1 3l7 6 7-6" fill="none" stroke="#fff" stroke-width="1.3"/></svg>
          <span>gideon@bravepathgrowth.com</span>
        </li>
        <li class="contact__item">
          <svg viewBox="0 0 16 16"><g fill="none" stroke="var(--navy)" stroke-width="1.4"><circle cx="8" cy="8" r="6.5"/><ellipse cx="8" cy="8" rx="3" ry="6.5"/><path d="M1.5 8h13M2.5 4.5h11M2.5 11.5h11"/></g></svg>
          <span>www.<span class="contact__web">bravepathgrowth</span>.com</span>
        </li>
      </ul>
    </div>

    <div class="back__seal"></div>
  </section>

</body>
</html>
```